Hydraulics Company Business Card Design

Modern business card design for a hydraulics company.
Our company colours are - black, orange and white.
I would like the following contact details included-
Name
Position
Phone number
Email
Website
Street Address

I have attached our company logo.
I would like the back of the card white.

Thank you.

```html
<!DOCTYPE html>
<html lang="en">
<head>
<meta charset="utf-8">
<title>Ridgeway Hydraulics – Business Card</title>
<link href="https://fonts.googleapis.com/css2?family=Montserrat:wght@400;500;700;800&display=swap" rel="stylesheet">
<style>
  :root {
    --orange: #f7941d;
    --black: #050505;
    --white: #ffffff;
    --ink: #1e1e1e;
    --stage: #2a2a2a;
  }
  * { margin: 0; padding: 0; box-sizing: border-box; }
  html, body { width: 1200px; height: 875px; overflow: hidden; }
  body {
    background: var(--stage);
    font-family: "Montserrat", sans-serif;
    display: flex;
    align-items: center;
    justify-content: center;
    gap: 48px;
  }
  .card {
    position: relative;
    width: 530px;
    height: 303px;
    border-radius: 20px;
    overflow: hidden;
  }
  .card--front {
    background: var(--black);
    display: flex;
    align-items: center;
    justify-content: center;
  }
  .brand {
    color: var(--orange);
    font-weight: 800;
    line-height: 1;
    letter-spacing: 0.5px;
    white-space: nowrap;
  }
  .card--front .brand { font-size: 42px; }
  .card--back { background: var(--white); color: var(--ink); }
  .card--back .brand {
    position: absolute;
    top: 30px;
    right: 28px;
    font-size: 22px;
  }
  .divider {
    position: absolute;
    left: 28px;
    right: 28px;
    top: 178px;
    height: 1px;
    background: var(--orange);
  }
  .person {
    position: absolute;
    left: 28px;
    bottom: 130px;
  }
  .person__name {
    color: var(--orange);
    font-weight: 800;
    font-size: 22px;
    line-height: 1.05;
  }
  .person__title {
    font-size: 11.5px;
    font-weight: 500;
    margin-top: 2px;
  }
  .contacts {
    position: absolute;
    left: 28px;
    top: 192px;
    list-style: none;
  }
  .contacts li {
    display: flex;
    align-items: center;
    gap: 8px;
    font-size: 11.5px;
    line-height: 1;
    margin-bottom: 8px;
  }
  .contacts svg { width: 11px; height: 11px; fill: var(--orange); flex: none; }
  .address {
    position: absolute;
    right: 28px;
    top: 196px;
    font-size: 11px;
    line-height: 1.35;
    text-align: right;
    font-style: normal;
  }
</style>
</head>
<body>
  <section class="card card--front" aria-label="Card front">
    <div class="brand">Ridgeway Hydraulics</div>
  </section>

  <section class="card card--back" aria-label="Card back">
    <div class="brand">Ridgeway Hydraulics</div>

    <div class="person">
      <div class="person__name">Daniel Reeve</div>
      <div class="person__title">Managing Director</div>
    </div>

    <div class="divider"></div>

    <ul class="contacts">
      <li>
        <svg viewBox="0 0 24 24" aria-hidden="true"><path d="M6.6 10.8a15.1 15.1 0 0 0 6.6 6.6l2.2-2.2a1 1 0 0 1 1-.25 11.4 11.4 0 0 0 3.6.57 1 1 0 0 1 1 1V20a1 1 0 0 1-1 1A17 17 0 0 1 3 4a1 1 0 0 1 1-1h3.5a1 1 0 0 1 1 1c0 1.25.2 2.45.57 3.57a1 1 0 0 1-.25 1z"/></svg>
        (08) 5550 2841
      </li>
      <li>
        <svg viewBox="0 0 24 24" aria-hidden="true"><path d="M2 5h20v14H2zm2 2v.5l8 5 8-5V7zm0 2.9V17h16V9.9l-8 5z"/></svg>
        hello@ridgewayhyd.com
      </li>
      <li>
        <svg viewBox="0 0 24 24" aria-hidden="true"><path d="M12 2a10 10 0 1 0 0 20 10 10 0 0 0 0-20zm6.9 6h-3a15 15 0 0 0-1.3-3.8A8 8 0 0 1 18.9 8zM12 4c.9 1.2 1.6 2.5 2 4h-4c.4-1.5 1.1-2.8 2-4zM4.3 14a8 8 0 0 1 0-4h3.4a16 16 0 0 0 0 4zm.8 2h3a15 15 0 0 0 1.3 3.8A8 8 0 0 1 5.1 16zm3-8h-3a8 8 0 0 1 4.3-3.8A15 15 0 0 0 8.1 8zM12 20c-.9-1.2-1.6-2.5-2-4h4c-.4 1.5-1.1 2.8-2 4zm2.3-6H9.7a14 14 0 0 1 0-4h4.6a14 14 0 0 1 0 4zm.3 5.8a15 15 0 0 0 1.3-3.8h3a8 8 0 0 1-4.3 3.8zm1.7-5.8a16 16 0 0 0 0-4h3.4a8 8 0 0 1 0 4z"/></svg>
        www.ridgewayhyd.com
      </li>
    </ul>

    <address class="address">48 Harbour Road,<br>Northvale, USA</address>
  </section>
</body>
</html>
```